Dark Comedy Movie Poster

We need a poster design for our short film BRAM that we just wrapped on.
It's a dark comedy
Bram explores the world of loneliness through the lens of a manic man-child. Bram wants nothing more than the approval of others, giving every last bit of energy to the cause. But his ravenous attempts accomplish the opposite, turning others off. His desperation is authentic, his lonliness cavernous.
Here is a link to the film
https://reelvault.example/847261093
Password: Bram41
I want you, the artist, to pitch me an idea in any way you want. I'm open to absolutely anything right now. Once I have some pitches from you all my production team and I will sort through them and pick the best fit!
-Olin

```html
<!DOCTYPE html>
<html lang="en">
<head>
<meta charset="utf-8">
<title>BRAM – Poster</title>
<link href="https://fonts.googleapis.com/css2?family=Amatic+SC:wght@400;700&family=Raleway:wght@600;700&display=swap" rel="stylesheet">
<style>
  :root {
    --teal: #2a8ca6;
    --teal-wash: #4aa3bb;
    --bg-letter: rgba(205, 236, 244, 0.72);
    --art-dark: #6f4c38;
    --art-warm: #c39070;
    --shirt-blue: #c6e6f3;
    --shirt-white: #fdfdfb;
    --shirt-yellow: #fbf6cf;
    --maroon: #7a1e1e;
  }
  * { margin: 0; padding: 0; box-sizing: border-box; }
  html, body { width: 848px; height: 1200px; overflow: hidden; background: #ffffff; }

  .poster {
    position: relative;
    width: 848px;
    height: 1200px;
    overflow: hidden;
    background: var(--teal);
  }

  .wash {
    position: absolute;
    left: 40px; top: 150px;
    width: 760px; height: 620px;
    background: radial-gradient(ellipse at 50% 45%, var(--teal-wash) 0%, rgba(74,163,187,0.6) 45%, rgba(42,140,166,0) 72%);
  }

  .message {
    position: absolute;
    left: 10px; top: 0;
    font-family: "Amatic SC", "Arial Narrow", sans-serif;
    color: var(--bg-letter);
    letter-spacing: 10px;
    line-height: 1;
    white-space: nowrap;
  }
  .message span { position: absolute; left: 0; }
  .message .l1 { top: 14px;  font-size: 96px; }
  .message .l2 { top: 168px; font-size: 100px; left: -6px; }
  .message .l3 { top: 306px; font-size: 104px; left: -30px; }
  .message .l4 { top: 460px; font-size: 110px; left: -24px; }
  .message .l5 { top: 640px; font-size: 150px; left: -16px; letter-spacing: 24px; }

  .shirt-art {
    position: absolute;
    left: 0; top: 860px;
    width: 848px; height: 340px;
    background: linear-gradient(90deg, var(--shirt-blue) 0%, var(--shirt-white) 40%, var(--shirt-white) 58%, var(--shirt-yellow) 78%, var(--shirt-yellow) 100%);
  }

  .portrait {
    position: absolute;
    left: 187px; top: 113px;
    width: 466px; height: 734px;
    background: linear-gradient(180deg, var(--art-dark) 0%, var(--art-warm) 100%);
  }

  .title {
    position: absolute;
    left: 0; width: 848px;
    top: 850px;
    text-align: center;
    font-family: "Amatic SC", cursive;
    font-weight: 400;
    font-size: 190px;
    line-height: 1;
    color: var(--maroon);
    letter-spacing: 0;
  }

  .credits {
    position: absolute;
    left: 0; width: 848px;
    top: 1058px;
    font-family: "Raleway", Arial, sans-serif;
    color: var(--maroon);
    text-align: center;
  }
  .credit { position: absolute; transform: translateX(-50%); white-space: nowrap; }
  .credit .role { display: block; font-size: 8px; font-weight: 600; letter-spacing: 0.3px; }
  .credit .name { display: block; font-weight: 700; }
  .credit.lead .name { font-size: 18px; margin-top: 5px; }
  .credit.crew .name { font-size: 13px; margin-top: 4px; }
  .credit.crew { top: 52px; }
</style>
</head>
<body>
<main class="poster">
  <div class="wash" aria-hidden="true"></div>

  <p class="message">
    <span class="l1">CONGRATS BRAM !</span>
    <span class="l2">YOU'VE ACCOMPLISHED</span>
    <span class="l3">ALL YOUR GOALS</span>
    <span class="l4">ALL ON YOUR OWN, WINNER</span>
    <span class="l5">SINCE DAY ONE</span>
  </p>

  <div class="shirt-art" role="img" aria-label="Painted shirt area in light blue, white and pale yellow watercolour"></div>

  <div class="portrait" role="img" aria-label="Painted portrait of the lead character"></div>

  <h1 class="title">BRAM</h1>

  <section class="credits">
    <div class="credit lead" style="left:220px; top:0;">
      <span class="role">STARRING</span><span class="name">REID CALLOWAY</span>
    </div>
    <div class="credit lead" style="left:437px; top:0;">
      <span class="role">WRITTEN &amp; DIRECTED</span><span class="name">OLIN MARKEL</span>
    </div>
    <div class="credit lead" style="left:607px; top:0;">
      <span class="role">STARRING</span><span class="name">JONAH PELL</span>
    </div>
    <div class="credit crew" style="left:307px;">
      <span class="role">DOP</span><span class="name">TOBIN ASHE</span>
    </div>
    <div class="credit crew" style="left:440px;">
      <span class="role">EDITOR</span><span class="name">CURTIS VALE</span>
    </div>
    <div class="credit crew" style="left:587px;">
      <span class="role">PRODUCED BY</span><span class="name">MILO BRANDT</span>
    </div>
  </section>
</main>
</body>
</html>
```